New Logo design and Business cards

We are changing our business name and require a new Logo and business card design. Our new name will be "Evergrove Garden Design & Construction" with a focus on enhancing our clients lifestyle through correct landscape design and construction of the designed landscape. We are a full service design to construct business meaning we take care of all aspects of designing and creating your ideal outdoor spaces. To see our current work and get a feel for what we do you can go to www.tallpinegardens.com.au. We do not wish to have a major change to the website only the name/logo should change with all current colours etc being used in the new logo and business card. For our Logo I want the logo to reflect who we now are, and what we do, however I want it to have minimal impact on the website with the aim to only need to change the Logo and not colours or text styles. With the business card I need there to be a strong link between the card and the website with colours and looks being similar. I would love to see an image of one of our projects to be included on the card even as a backdrop. I have included a photo that I think could be used in the background of the business card. I have attached a copy of our current business cards (so you with have all relevant information required on the new cards) though I do want a fresh look with strong links to our website. Please feel free to contact me if you have any questions or ideas.

Construction

Evergrove Garden Design & Construction-Bringing outdoor living home.

```html
<!DOCTYPE html>
<html lang="en">
<head>
<meta charset="utf-8">
<title>Evergrove Garden Design &amp; Construction – Logo and Business Card Options</title>
<link href="https://fonts.googleapis.com/css2?family=Tinos:wght@400;700&family=Oswald:wght@400;500&family=Arimo:wght@700&display=swap" rel="stylesheet">
<style>
  :root {
    --page: #ffffff;
    --ink: #000000;
    --body: #1a1a1a;
    --card-top: #c9ccd2;
    --card-mid: #8fa3bd;
    --card-low: #b4b2ad;
    --card-edge: #7d7d7d;
  }
  * { margin: 0; padding: 0; box-sizing: border-box; }
  html, body { width: 848px; height: 1200px; overflow: hidden; background: var(--page); }
  .sheet { position: relative; width: 848px; height: 1200px; background: var(--page); color: var(--body); font-family: "Tinos", "Times New Roman", serif; }
  .note { position: absolute; left: 84px; width: 680px; font-size: 13.2px; line-height: 16.6px; }
  .note--logo { top: 94px; }
  .note--cards { top: 472px; }
  .option-label { position: absolute; left: 88px; font-size: 13px; }
  .option-label--one { top: 557px; }
  .option-label--two { top: 839px; left: 84px; }

  .logo { position: absolute; color: var(--ink); font-family: "Oswald", "Arial Narrow", sans-serif; font-weight: 500; }
  .logo__mark { position: absolute; border-radius: 50%; background: var(--ink); }
  .logo__name { position: absolute; white-space: nowrap; line-height: 1; }
  .logo__line { position: absolute; white-space: nowrap; line-height: 1; }

  .logo--plain { left: 103px; top: 200px; width: 300px; height: 140px; }
  .logo--plain .logo__mark { left: 8px; top: 4px; width: 56px; height: 56px; }
  .logo--plain .logo__name { left: 74px; top: 2px; font-size: 56px; }
  .logo--plain .logo__line { left: 2px; top: 92px; font-size: 26px; letter-spacing: -0.6px; }

  .logo--slogan { left: 440px; top: 203px; width: 300px; height: 160px; }
  .logo--slogan .logo__mark { left: 6px; top: 4px; width: 56px; height: 56px; }
  .logo--slogan .logo__name { left: 72px; top: 2px; font-size: 56px; }
  .logo--slogan .logo__line { left: 0; width: 280px; text-align: center; font-size: 21px; }
  .logo--slogan .logo__line--first { top: 104px; }
  .logo--slogan .logo__line--second { top: 130px; }

  .card { position: absolute; left: 90px; width: 348px; height: 177px; overflow: hidden; box-shadow: 1px 1px 3px var(--card-edge); color: var(--ink); font-family: "Arimo", Arial, sans-serif; font-weight: 700; }
  .card--one { top: 603px; }
  .card--two { top: 881px; }
  .card__photo { position: absolute; inset: 0; background: linear-gradient(180deg, var(--card-top) 0%, var(--card-mid) 42%, var(--card-low) 70%, var(--card-top) 100%); }
  .card__text { position: absolute; white-space: nowrap; line-height: 1.05; }
  .card__mark { position: absolute; border-radius: 50%; background: var(--ink); }
  .card__brand { position: absolute; white-space: nowrap; font-family: "Oswald", "Arial Narrow", sans-serif; font-weight: 500; line-height: 1; }
  .card__serif { position: absolute; white-space: nowrap; font-family: "Tinos", "Times New Roman", serif; font-weight: 400; line-height: 1; }
  .right { text-align: right; }
  .rule { position: absolute; height: 1px; background: var(--ink); }
</style>
</head>
<body>
<main class="sheet">
  <p class="note note--logo">Logo - No 1 - Strong design yet simple, less is more. I did not include the slogan “Bringing outdoor living home” in the 1st LOGO, as “Evergrove” already says it in the Logo. However it is Option 2 . I have kept your circle, although in Option 2 it is slightly different (slight) but as you wanted the photograph implemented in the Business Cards, the strong Black lines of the Logo makes a statement and fits the “style” category.</p>

  <div class="logo logo--plain">
    <span class="logo__mark"></span>
    <span class="logo__name">Evergrove</span>
    <span class="logo__line">Garden Design &amp; Construction.</span>
  </div>

  <div class="logo logo--slogan">
    <span class="logo__mark"></span>
    <span class="logo__name">Evergrove</span>
    <span class="logo__line logo__line--first">Garden Design &amp; Construction.</span>
    <span class="logo__line logo__line--second">"Bringing outdoor living home"</span>
  </div>

  <p class="note note--cards">Business Cards - Option 1 &amp; Option 2 - I have used the photograph as requested, though faded and artistically manipulated. They are both slightly different in setup.</p>

  <p class="option-label option-label--one">Option 1 - —Size 86.99mm x 45.49mm</p>

  <section class="card card--one">
    <div class="card__photo" role="img" aria-label="Faded, artistically treated photograph of a finished outdoor living project with pool and lounge area"></div>
    <span class="card__mark" style="left:14px;top:14px;width:24px;height:24px;"></span>
    <span class="card__brand" style="left:44px;top:11px;font-size:28px;">Evergrove</span>
    <span class="card__brand" style="left:14px;top:52px;font-size:13px;">Garden Design &amp; Construction.</span>
    <span class="card__text right" style="right:8px;top:24px;font-size:11px;">"Bringing outdoor living home".</span>
    <span class="card__text right" style="right:8px;top:46px;font-size:20px;">Dana Hollis</span>
    <span class="card__text" style="left:272px;top:70px;font-size:7px;">Director</span>
    <div class="card__text right" style="right:8px;top:88px;font-size:8px;line-height:9px;">
      CAD design incl. 3D<br>Structural Landscaping<br>Decks, Gazebo's, Excavation.<br>ABN 52 608 117 940<br>ACN 608 117 940<br>QBSA Lic No. 12 48019<br>Master Builders 30742<br>Landscape QD No. 527<br>AILDM No. 688
    </div>
    <div class="card__brand" style="left:14px;top:114px;font-size:12px;line-height:15px;">Tel: 04-210 48 397<br>Fax: 07 3190 2265</div>
    <div class="card__brand" style="left:14px;top:145px;font-size:11px;line-height:13px;">dana@tallpinegardens.com.au<br>www.tallpinegardens.com.au</div>
  </section>

  <p class="option-label option-label--two">Option 2—Size 86.99mm x 45.49mm</p>

  <section class="card card--two">
    <div class="card__photo" role="img" aria-label="Faded, artistically treated photograph of a finished outdoor living project with pool and lounge area"></div>
    <span class="card__mark" style="left:3px;top:11px;width:28px;height:28px;"></span>
    <span class="card__brand" style="left:36px;top:6px;font-size:30px;">Evergrove</span>
    <span class="card__brand right" style="right:6px;top:8px;font-size:16px;letter-spacing:-0.4px;">Garden Design &amp; Construction.</span>
    <span class="card__serif right" style="right:10px;top:30px;font-size:16px;">Bringing outdoor living home</span>
    <span class="rule" style="left:160px;top:52px;width:184px;"></span>
    <span class="card__text" style="left:190px;top:58px;font-size:17px;">Dana Hollis</span>
    <span class="card__text" style="left:236px;top:78px;font-size:7px;">Director</span>
    <div class="card__text" style="left:6px;top:62px;font-size:9px;line-height:10.5px;">CAD design incl. 3D<br>Structural Landscaping<br>Decks, Gazebo's, Excavation.</div>
    <div class="card__text" style="left:6px;top:123px;font-size:7.8px;line-height:8.4px;">ABN 52 608 117 940<br>ACN 608 117 940<br>QBSA Lic No. 12 48019<br>Master Builders 30742<br>Landscape QD No. 527<br>AILDM No. 688</div>
    <div class="card__brand right" style="right:4px;top:124px;font-size:10px;line-height:12px;">Tel: 04-210 48 397<br>Fax: 07 3190 2265<br>dana@tallpinegardens.com.au<br>www.tallpinegardens.com.au</div>
  </section>
</main>
</body>
</html>
```